integrative health clinic-Medical massage, acupuncture, chiropractic

we like our logo, but are open to new ideas. We need a new card design. We have added chiropractic and acupuncture that we have put under the name of the business. We are an integrative medical clinic

Target Market(s)

General public, athletes

Contact Information for Business Card

Phone 5055583927
Fax 5055583926
Hours Monday-Friday 9-6
Saturday 10-6
The 20% can be smaller on the back

Colors
3176b5
0355a3

Requirements
Must have
• Logo but am open to ideas
Nice to have
• We are an integrated medical clinic but also want to be personable. We want the card fun and inviting

```html
<!DOCTYPE html>
<html lang="en">
<head>
<meta charset="utf-8">
<title>Open River Wellness – Business Card</title>
<link href="https://fonts.googleapis.com/css2?family=Montserrat:wght@300;400;500;600;700;800&family=Roboto+Condensed:wght@600&display=swap" rel="stylesheet">
<style>
  :root {
    --indigo: #2e3192;
    --indigo-mid: #4a4aa0;
    --lavender: #a8a6d6;
    --lavender-pale: #e2e0f1;
    --back-end: #6565ab;
    --ink: #1c1c1c;
    --white: #ffffff;
    --shadow: #2b2b2b;
    --page: #ffffff;
  }
  * { margin: 0; padding: 0; box-sizing: border-box; }
  html, body {
    width: 1200px; height: 1200px; overflow: hidden;
    background: var(--page);
    font-family: "Montserrat", sans-serif;
  }
  .canvas { position: relative; width: 1200px; height: 1200px; border: 1px solid var(--ink); }
  .card {
    position: absolute; left: 223px; width: 759px; height: 456px;
    box-shadow: 5px 5px 0 var(--shadow);
    overflow: hidden;
  }
  .card-front { top: 136px; background: var(--white); border: 1px solid var(--ink); }
  .card-back {
    top: 666px;
    background: linear-gradient(160deg, var(--indigo) 0%, var(--back-end) 100%);
    color: var(--white); text-align: center;
  }

  /* Front */
  .brand { position: absolute; left: 0; width: 100%; top: 74px; text-align: center; }
  .brand-name {
    display: inline-flex; align-items: center; gap: 12px;
    font-size: 40px; font-weight: 600; color: var(--ink); letter-spacing: -0.5px;
  }
  .brand-dot { width: 22px; height: 22px; border-radius: 50%; background: var(--indigo); }
  .brand-tagline { margin-top: 6px; font-size: 19px; font-weight: 400; color: var(--ink); }
  .services {
    position: absolute; left: 0; width: 100%; top: 186px; text-align: center;
    font-size: 31px; font-weight: 600; color: var(--indigo);
  }
  .wave { position: absolute; left: 0; top: 0; width: 100%; height: 100%; }
  .contact { position: absolute; inset: 0; color: var(--white); font-size: 16px; font-weight: 500; white-space: nowrap; }
  .contact-line { position: absolute; right: 60px; transform: translateY(-50%); }
  .contact-icon { position: absolute; right: 26px; transform: translateY(-50%); width: 22px; height: 22px; }
  .phone { top: 341px; } .fax { top: 372px; } .email { top: 400px; }
  .address { position: absolute; left: 16px; top: 400px; transform: translateY(-50%); font-weight: 400; font-size: 16.5px; }
  .pin { position: absolute; left: 186px; top: 351px; width: 22px; height: 26px; }

  /* Back */
  .book-title { position: absolute; left: 0; width: 100%; top: 100px; font-size: 46px; font-weight: 800; }
  .book-url { position: absolute; left: 0; width: 100%; top: 164px; font-size: 25px; font-weight: 600; }
  .offer {
    position: absolute; left: 0; width: 100%; top: 200px;
    font-family: "Roboto Condensed", sans-serif; font-size: 20px; font-weight: 600;
  }
  .hours { position: absolute; left: 0; width: 100%; top: 247px; font-size: 27px; font-weight: 300; line-height: 38px; }
  .specialties { position: absolute; left: 0; width: 100%; top: 359px; font-size: 21px; font-weight: 300; }
</style>
</head>
<body>
<div class="canvas">

  <section class="card card-front">
    <svg class="wave" viewBox="0 0 1122 674" preserveAspectRatio="none" aria-hidden="true">
      <defs>
        <linearGradient id="bandFade" x1="0" y1="0" x2="1" y2="0">
          <stop offset="0" stop-color="#4a4aa0"/>
          <stop offset="0.55" stop-color="#8c88c4"/>
          <stop offset="1" stop-color="#e2e0f1"/>
        </linearGradient>
        <linearGradient id="baseFade" x1="0" y1="0" x2="1" y2="0">
          <stop offset="0" stop-color="#a8a6d6"/>
          <stop offset="0.4" stop-color="#6f6ab0"/>
          <stop offset="0.72" stop-color="#2e3192"/>
          <stop offset="1" stop-color="#2e3192"/>
        </linearGradient>
      </defs>
      <path d="M0 391 C170 430 300 452 420 447 C640 440 780 378 930 370 C1020 366 1080 378 1122 390 L1122 674 L0 674 Z" fill="url(#bandFade)"/>
      <path d="M0 422 C170 462 300 480 420 478 C640 472 780 404 920 398 C1010 394 1080 408 1122 420 L1122 674 L0 674 Z" fill="url(#baseFade)"/>
    </svg>

    <div class="brand">
      <div class="brand-name"><span class="brand-dot"></span>Open River Wellness</div>
      <div class="brand-tagline">Sports Therapy and Wellness Center</div>
    </div>
    <div class="services">Acupuncture and Chiropractic</div>

    <div class="contact">
      <svg class="pin" viewBox="0 0 22 26" aria-hidden="true">
        <path d="M11 0C5 0 1 4.4 1 9.8 1 16.5 11 26 11 26s10-9.5 10-16.2C21 4.4 17 0 11 0z" fill="#fff"/>
        <circle cx="11" cy="10" r="4" fill="#8e89c5"/>
      </svg>
      <span class="address">1480 Cedar Lane, H2 Santa Fe NM, 87501</span>

      <span class="contact-line phone">(505) 558 3927</span>
      <svg class="contact-icon phone" viewBox="0 0 24 24" aria-hidden="true">
        <path d="M6.6 2.5l3 3.6-1.9 2.4c1.3 2.8 3.6 5.1 6.4 6.4l2.4-1.9 3.6 3-1.5 3.8C11 19.5 4.5 13 3 4z" fill="#fff"/>
      </svg>

      <span class="contact-line fax">5055583926</span>
      <svg class="contact-icon fax" viewBox="0 0 24 24" aria-hidden="true">
        <rect x="6" y="1" width="12" height="8" fill="none" stroke="#fff" stroke-width="2"/>
        <rect x="2" y="10" width="20" height="13" fill="#fff"/>
        <rect x="4" y="17" width="3" height="3" fill="#2e3192"/>
      </svg>

      <span class="contact-line email">info@openriverwellness.com</span>
      <svg class="contact-icon email" viewBox="0 0 24 24" aria-hidden="true">
        <path d="M2 21V3h4l6 8 6-8h4v18h-4V10l-6 7-6-7v11z" fill="#fff"/>
      </svg>
    </div>
  </section>

  <section class="card card-back">
    <h2 class="book-title">Book Online</h2>
    <p class="book-url">www.openriverwellness.com</p>
    <p class="offer">20% OFF First Visit</p>
    <p class="hours">Mon-Fri 9-6<br>Sat 10-6</p>
    <p class="specialties">Specializing in Medical, Sports Massage and Manual Therapies</p>
  </section>

</div>
</body>
</html>
```